依頼詳細
サイト構成・基本的な要件については
https://zumora.example/diagrams/P3TR8xmaqelu2sHb
を併せてご覧いただければ幸いです。
※導線が確保されていれば、必ずしもレイアウト案に忠実である必要はございません。
ぜひご提案いただければ幸甚です。

また、素材については
http://nibulo-share.example/download/58174a2c9d3e0b6f1a7c4e2d9b8f0a6c3e5d7b1f
よりダウンロードいただければと存じます。

上記だけで制作が難しい場合は
http://moruka.example/
などから、5000円程度までならこちらにて購入可能です。カンプデータにて作成頂き、
納品時に当方にて購入したデータに差し替えていただければと存じます。

全体的なデザインのイメージとしては

http://www.tovira-hatake.example/
http://www.samolet.example/rollmode/
http://vesmira.example/
http://ri-kogetsu.example/
のような、白ベースですっきりと見やすい印象が希望です。

メインカラーは既存サイトと同様、グリーンでお願いします。
http://www.tobakitchen.example/
サイトURL
ページ数
1ページ
希望イメージ
シンプル 複雑
単色 カラフル
暗い 明るい
日常 高級
遊び心 厳粛
未来的 伝統的
女性的 男性的
希望する色
白を基調とし、グリーンベースでスッキリと明るく見やすいデザインを希望します
納品ファイル
• 高解像度JPG (.jpg)
• フォトショップ形式 (.psd)
補足説明
素材については
よりダウンロードいただければと存じます。

上記だけで制作が難しい場合は
http://moruka.example/

白ベースでメインカラーは既存と同様にグリーンを使用し、
明るく見やすいデザインをお願いできればと思います。

http://bottom-parts.example/2012/166.html
http://bottom-parts.example/2011/115.html
→フッター部分の参照

基本レイアウト
については、必ずしも忠実である必要はありません。

是非ご提案お待ちしております。
何卒よろしくお願いいたします。

制作につきましてご不明な点がございましたら、お気軽にお申し付けいただければと存じます。
ご提案お待ちしております。

クライアント様との協議の結果こちらの案を採用させていただきました。
高級感と柔らかさのバランスがとてもよく、
視認性も高く、要望を全て満たしておりましたので
こちらの案を採用いたしました。

この度は多数ご提案いただきありがとうございました。
当選に至らなかったランサー様におかれましては大変心苦しいのですが、
またの機会にぜひご提案いただければ幸甚です。
引き続き何卒よろしくお願いいたします。

```html
<!DOCTYPE html>
<html lang="ja">
<head>
<meta charset="utf-8">
<title>トバキッチン</title>
<link rel="stylesheet" href="https://fonts.googleapis.com/css2?family=Noto+Sans+JP:wght@400;700&display=swap">
<style>
:root{
  --green:#3d9a2f;
  --green-dark:#2e7d22;
  --green-light:#e6f2dd;
  --line:#9ccc8a;
  --text:#444;
  --red:#d9352b;
  --orange:#ef8a1a;
  --magenta:#c2367a;
  --leaf:#58a531;
  --amber:#f0a21b;
  --yellow:#e3c21b;
  --photo-a:#e7dccb;
  --photo-b:#b9a58a;
}
*{box-sizing:border-box;margin:0;padding:0}
html,body{width:900px;height:1200px;overflow:hidden;background:#fff}
body{font-family:"Noto Sans JP",sans-serif;color:var(--text);font-size:12px;position:relative}
ul{list-style:none}

.site-header{position:absolute;left:24px;top:0;width:852px;height:112px}
.brand{position:absolute;left:0;top:14px;display:flex;align-items:center;gap:10px}
.brand-mark{width:40px;height:40px;border-radius:50%;background:var(--green)}
.brand-name{font-size:26px;font-weight:700;color:var(--green-dark);line-height:1.1}
.brand-sub{font-size:12px;font-weight:700;color:var(--green-dark)}
.branches{position:absolute;left:600px;top:8px}
.branches li{font-size:13px;font-weight:700;color:var(--text);height:20px;display:flex;align-items:center;gap:6px}
.branches li span{background:var(--red);color:#fff;font-size:9px;padding:0 5px;border-radius:2px}
.trial-box{position:absolute;right:0;top:6px;width:98px;height:68px;border:2px solid var(--green);background:#fff;color:var(--red);font-size:11px;font-weight:700;text-align:center;padding-top:10px;line-height:1.4}

.global-nav{position:absolute;left:24px;top:120px;width:852px;height:30px;background:var(--green);display:flex;align-items:center}
.global-nav a{color:#fff;text-decoration:none;font-size:12px;font-weight:700;padding:0 24px;border-right:1px solid rgba(255,255,255,.5);line-height:14px}
.global-nav a:last-child{border-right:0}

.hero{position:absolute;left:24px;top:162px;width:852px;height:336px;background:linear-gradient(120deg,#cdd5cf 0%,#efe8da 45%,#d9cbb3 100%)}
.hero-copy{position:absolute;left:26px;top:220px;color:#fff;font-size:24px;font-weight:700;line-height:1.45;text-shadow:0 1px 4px rgba(0,0,0,.35)}

.side{position:absolute;left:24px;top:528px;width:228px}
.trial-panel{background:var(--green);color:#fff;text-align:center;padding:10px 0 12px;line-height:1.45}
.trial-panel .lead{font-size:13px;font-weight:700}
.trial-panel dt{font-size:12px;margin-top:4px}
.trial-panel dd{font-size:15px;font-weight:700}
.side-heading{margin-top:22px;font-size:14px;font-weight:700;color:var(--green-dark);border-bottom:2px solid var(--green);padding-bottom:4px}
.side-menu li{font-size:12px;padding:6px 0 6px 16px;border-bottom:1px dotted var(--line);position:relative}
.side-menu li::before{content:"";position:absolute;left:4px;top:12px;border-left:5px solid var(--green);border-top:4px solid transparent;border-bottom:4px solid transparent}
.corporate{margin-top:24px;height:40px;background:linear-gradient(90deg,var(--green) 0 60%,#a7c79a);color:#fff;font-size:13px;font-weight:700;display:flex;align-items:center;padding-left:12px}

.main{position:absolute;left:272px;top:528px;width:604px}
.section-title{font-size:14px;font-weight:700;color:var(--green-dark);border-bottom:2px solid var(--green);padding-bottom:4px}
.courses{display:grid;grid-template-columns:1fr 1fr;gap:12px 14px;margin-top:14px}
.course{height:108px;display:flex;flex-direction:column}
.course h3{height:32px;color:#fff;font-size:14px;font-weight:700;display:flex;align-items:center;justify-content:center}
.course .photo{flex:1;background:linear-gradient(135deg,var(--photo-a),var(--photo-b))}
.c-red h3{background:var(--red)} .c-orange h3{background:var(--orange)}
.c-magenta h3{background:var(--magenta)} .c-leaf h3{background:var(--leaf)}
.c-amber h3{background:var(--amber)} .c-yellow h3{background:var(--yellow)}
.info{display:grid;grid-template-columns:1fr 1fr;gap:14px;margin-top:22px}
.info li{font-size:10px;line-height:1.7;white-space:nowrap}
.info li span{color:var(--green-dark);margin-right:8px}

.site-footer{position:absolute;left:24px;top:1042px;width:852px}
.footer-links{border-top:3px solid var(--green);background:var(--green-light);display:grid;grid-template-columns:repeat(4,1fr);padding:10px 20px;height:116px}
.footer-links h4{font-size:11px;color:var(--green-dark);margin-bottom:3px}
.footer-links li{font-size:9.5px;line-height:1.6}
.copyright{background:var(--green);color:#fff;font-size:10px;text-align:center;height:22px;line-height:22px;margin-top:8px}
</style>
</head>
<body>
<header class="site-header">
  <div class="brand">
    <div class="brand-mark"></div>
    <div><div class="brand-name">トバキッチン</div><div class="brand-sub">Toba Kitchen School</div></div>
  </div>
  <ul class="branches">
    <li>本町校 <span>map</span></li>
    <li>川辺校 <span>map</span></li>
    <li>駅前校 <span>map</span></li>
  </ul>
  <div class="trial-box">体験レッスン<br>受講受付中！<br>お申し込み</div>
</header>

<nav class="global-nav">
  <a>HOME</a><a>トバキッチンについて</a><a>コース案内</a><a>入会案内</a><a>よくあるご質問</a>
</nav>

<div class="hero" role="img" aria-label="卵をボウルに割り入れる手元の写真">
  <p class="hero-copy">ひとりCookingだから<br>上手くなれる。</p>
</div>

<aside class="side">
  <div class="trial-panel">
    <p class="lead">体験レッスン<br>受付中！</p>
    <dl>
      <dt>本町校</dt><dd>03-4812-0735</dd>
      <dt>川辺校</dt><dd>03-4812-0951</dd>
      <dt>駅前校</dt><dd>03-4812-1164</dd>
    </dl>
  </div>
  <h2 class="side-heading">コンテンツ</h2>
  <ul class="side-menu">
    <li>HOME</li><li>トバキッチンについて</li><li>コース案内</li><li>入会案内</li><li>よくあるご質問</li><li>お問い合わせ</li>
  </ul>
  <div class="corporate" role="img" aria-label="企業向け案内バナー">企業のみなさまへ</div>
</aside>

<main class="main">
  <h2 class="section-title">コース紹介</h2>
  <div class="courses">
    <div class="course c-red"><h3>トバキッチンの特徴</h3><div class="photo" role="img" aria-label="料理写真"></div></div>
    <div class="course c-orange"><h3>レギュラーコース</h3><div class="photo" role="img" aria-label="料理写真"></div></div>
    <div class="course c-magenta"><h3>専門・特別コース</h3><div class="photo" role="img" aria-label="料理写真"></div></div>
    <div class="course c-leaf"><h3>短期集中コース</h3><div class="photo" role="img" aria-label="料理写真"></div></div>
    <div class="course c-amber"><h3>サンデーコース</h3><div class="photo" role="img" aria-label="料理写真"></div></div>
    <div class="course c-yellow"><h3>男性コース</h3><div class="photo" role="img" aria-label="料理写真"></div></div>
  </div>
  <div class="info">
    <div>
      <h2 class="section-title">新着情報</h2>
      <ul>
        <li><span>2014.3.8</span>体験レッスンのお知らせ</li>
        <li><span>2014.3.5</span>春の特別講座を開講します</li>
        <li><span>2014.3.1</span>フランス料理コース募集</li>
      </ul>
    </div>
    <div>
      <h2 class="section-title">今月のメニュー</h2>
      <ul>
        <li><span>2014.3.8</span>和食基礎 煮物と汁物</li>
        <li><span>2014.3.5</span>洋食基礎 ハンバーグ</li>
        <li><span>2014.3.1</span>春の焼き菓子</li>
      </ul>
    </div>
  </div>
</main>

<footer class="site-footer">
  <div class="footer-links">
    <div><h4>トバキッチン</h4><ul><li>HOME</li><li>トバキッチンについて</li><li>スクール紹介</li><li>講師紹介</li><li>よくあるご質問</li></ul></div>
    <div><h4>コース案内</h4><ul><li>レギュラーコース</li><li>専門・特別コース</li><li>短期集中コース</li><li>サンデーコース</li><li>男性コース</li></ul></div>
    <div><h4>入会案内</h4><ul><li>体験レッスン</li><li>入会方法</li><li>料金案内</li><li>企業のみなさまへ</li></ul></div>
    <div><h4>その他</h4><ul><li>お問い合わせ</li><li>プライバシーポリシー</li><li>サイトマップ</li></ul></div>
  </div>
  <p class="copyright">Copyright©Toba Kitchen All Right Reserved.</p>
</footer>
</body>
</html>
```